A property investment company, looking to provide lovely sustainable homes for familys and individua

For a small investment business i am starting which will buy and refurbish unloved houses and apartments to rent out or resell. the company name is my family surname (HARGREAVE). <br/>i would like the design to be simple with maybe some emphasis on an ethical and sustainable/environmentally friendly approach with a branding of maybe trees blended with some houses and or apartments.<br/>The colours i like for this design would be mainly green on either a white or black background.
Target Market(s)
This business card is to be used for professional people such as estate agents
mortgage brokers, solicitors and trades people.
Industry/Entity Type
Real Estate
Contact Information for Business Card
owner/director-Martin hargreave
e-mail-martin@hvholdings.co.uk
website-hargreavehomeholdings.co.uk
mobile-07700945318
landline-02079460581
Look and feel

```html
<!DOCTYPE html>
<html lang="en">
<head>
<meta charset="utf-8">
<title>Hargreave Property – Business Card</title>
<link href="https://fonts.googleapis.com/css2?family=Montserrat:wght@400;500;700&display=swap" rel="stylesheet">
<style>
  :root {
    --teal: #27b9a4;
    --ink: #1a1a1a;
    --muted: #444444;
    --faint: #d9dcdc;
    --rule: #9a9a9a;
    --paper: #ffffff;
    --backdrop: #ececec;
  }
  * { margin: 0; padding: 0; box-sizing: border-box; }
  html, body { width: 1145px; height: 1200px; overflow: hidden; }
  body {
    background: var(--backdrop);
    font-family: "Montserrat", sans-serif;
    position: relative;
  }
  .card {
    position: absolute;
    left: 122px;
    width: 900px;
    height: 539px;
    background: var(--paper);
    overflow: hidden;
    box-shadow: 0 10px 30px rgba(0,0,0,0.12);
  }
  .card--front { top: 41px; }
  .card--back { top: 620px; }
  .abs { position: absolute; }

  /* front */
  .front__band { left: 0; top: 0; width: 94px; height: 100%; background: var(--teal); }
  .front__stripe { left: 103px; top: 0; width: 5px; height: 100%; background: var(--teal); }
  .front__company { right: 160px; top: 82px; font-size: 13px; color: var(--ink); }
  .front__rule { left: 427px; width: 313px; height: 1px; background: var(--rule); }
  .front__rule--top { top: 266px; }
  .front__rule--bottom { top: 408px; }
  .front__brand {
    right: 505px; top: 318px;
    display: flex; align-items: center; gap: 10px;
    font-size: 24px; font-weight: 700; color: var(--teal);
  }
  .front__brand-dot { width: 14px; height: 14px; border-radius: 50%; background: var(--teal); }
  .front__name { left: 490px; top: 291px; font-size: 35px; font-weight: 700; color: var(--ink); white-space: nowrap; }
  .front__title { left: 492px; top: 338px; font-size: 21px; font-weight: 400; color: var(--muted); }
  .front__name, .front__title { left: 491px; }

  /* back */
  .back__band { right: 0; top: 0; width: 70px; height: 100%; background: var(--teal); }
  .back__block { left: 0; top: 186px; width: 50px; height: 166px; background: var(--teal); }
  .back__brand { left: 85px; top: 120px; font-size: 46px; font-weight: 700; color: var(--faint); }
  .back__company { left: 85px; top: 403px; font-size: 35px; font-weight: 700; color: var(--faint); }
  .back__name { left: 504px; top: 110px; font-size: 35px; font-weight: 700; color: var(--ink); }
  .back__title { left: 504px; top: 148px; font-size: 22px; color: var(--muted); }
  .back__contacts { left: 504px; top: 214px; font-size: 16px; color: var(--ink); line-height: 21px; list-style: none; }
  .back__contacts li.gap { margin-top: 19px; }
  .back__rule { left: 504px; width: 298px; height: 3px; background: var(--teal); }
  .back__rule--one { top: 413px; }
  .back__rule--two { top: 430px; }
</style>
</head>
<body>
  <section class="card card--front" aria-label="Business card front">
    <div class="abs front__band"></div>
    <div class="abs front__stripe"></div>
    <p class="abs front__company">Hargreave Property</p>
    <div class="abs front__rule front__rule--top"></div>
    <div class="abs front__brand"><span class="front__brand-dot"></span>Hargreave</div>
    <h1 class="abs front__name">Martin Hargreave</h1>
    <p class="abs front__title">Director</p>
    <div class="abs front__rule front__rule--bottom"></div>
  </section>

  <section class="card card--back" aria-label="Business card back">
    <div class="abs back__block"></div>
    <div class="abs back__brand">Hargreave</div>
    <p class="abs back__company">Hargreave Property</p>
    <h2 class="abs back__name">Martin Hargreave</h2>
    <p class="abs back__title">Director</p>
    <ul class="abs back__contacts">
      <li>07700945318 (Mobile )</li>
      <li>02079460581 (Landline )</li>
      <li class="gap">martin@hvholdings.co.uk</li>
      <li class="gap">hargreavehomeholdings.co.uk</li>
    </ul>
    <div class="abs back__rule back__rule--one"></div>
    <div class="abs back__rule back__rule--two"></div>
    <div class="abs back__band"></div>
  </section>
</body>
</html>
```